Ad designs for TalkHive and Lumora

We are a company that buy and sell airlines miles.
We publish our Ads on TH and Lumora and wish to receive 10 designs that reflects our business with some texts. Please see some examples.
10 designs with includes some text in English and those same 10 designs with include a text in Hebrew (written from right to left).
We need each of the designs to eventually be created at the following ratios and resolutions:
Square format (1:1): 1080 x 1080 pixels
Vertical format (9:16): 1080 x 1920 pixels
Horizontal format (16:9): 1280 x 720 pixels
Vertical video format (4:5): 1080 x 1350 pixels
Please see the samples sent and our login as well attached
Texts in English:
"We buy your airline miles for"
or
"Sell us your airline miles"
or
"Receive money for your airline miles"

and in Hebrew:
"אנחנו קונים את הנקודות שלכם בחברות התעופה"
or
"קונים נקודות נוסע מתמיד תמורת מזומן"
or
"קונים נקודות טל גן וחברות אחרות"

Please add a red button to all Ads in Eng saying "Get Quote"
and in Heb saying "להצעת מחיר"

```html
<!DOCTYPE html>
<html lang="en">
<head>
<meta charset="utf-8">
<title>Milora – Sell us your airline miles – ad formats</title>
<link rel="stylesheet" href="https://fonts.googleapis.com/css2?family=Poppins:wght@400;700;800&family=Playfair+Display:ital@1&display=swap">
<style>
  :root {
    --board: #c3c3c3;
    --label: #2a2a2a;
    --sky-top: #2a2fe0;
    --sky-mid: #2f3fa8;
    --sky-haze: #8d88b4;
    --sky-glow: #e9b99a;
    --cloud: #9a7468;
    --floor: #ffffff;
    --navy: #13206b;
    --red: #d8101f;
    --white: #ffffff;
    --ink: #1b1b1b;
    --subject-a: #e9edf3;
    --subject-b: #6d9fd4;
    --subject-c: #c23a3a;
  }
  * { margin: 0; padding: 0; box-sizing: border-box; }
  html, body { width: 960px; height: 1200px; overflow: hidden; }
  body { background: var(--board); font-family: "Poppins", Arial, sans-serif; position: relative; }

  .ad {
    position: absolute;
    overflow: hidden;
    background: var(--floor);
    box-shadow: 0 4px 14px rgba(0,0,0,.18);
  }
  .ad--square    { left: 44.5px;  top: 83px;    width: 360.6px; height: 360.6px; }
  .ad--story     { left: 489.7px; top: 83px;    width: 360.6px; height: 641px; }
  .ad--portrait  { left: 44.5px;  top: 600.5px; width: 360.6px; height: 450.8px; }
  .ad--landscape { left: 489.7px; top: 810.8px; width: 427.4px; height: 240.4px; }

  .ad__sky {
    position: absolute; left: 0; top: 0; width: 100%;
    background: linear-gradient(180deg, var(--sky-top) 0%, var(--sky-mid) 28%, var(--sky-haze) 55%, var(--sky-glow) 78%, var(--cloud) 100%);
  }
  .ad__subject {
    position: absolute;
    border-radius: 46% 46% 10% 10% / 30% 30% 6% 6%;
    background: linear-gradient(180deg, var(--subject-a) 0%, var(--subject-b) 45%, var(--subject-a) 70%, var(--subject-c) 100%);
    opacity: .92;
  }

  .brand {
    position: absolute;
    color: var(--white); font-weight: 700; letter-spacing: .02em; line-height: 1;
    white-space: nowrap;
  }

  .headline { position: absolute; text-align: center; line-height: 1; }
  .headline__sell { display: block; color: var(--white); font-weight: 400; }
  .headline__your { display: block; color: var(--navy); font-family: "Playfair Display", Georgia, serif; font-style: italic; }
  .headline__airline { display: block; color: var(--navy); font-weight: 800; letter-spacing: -.02em; }
  .headline__miles { display: block; color: var(--red); font-weight: 800; letter-spacing: -.03em; }

  .cta {
    position: absolute; display: flex; align-items: center; justify-content: center;
    background: var(--red); color: var(--white); border-radius: 999px; font-weight: 400;
    white-space: nowrap;
  }

  .size-label {
    position: absolute; color: var(--label); font-size: 24.5px; font-weight: 400;
    transform: translateX(-50%); white-space: nowrap; line-height: 1;
  }
</style>
</head>
<body>

  <!-- 1:1 -->
  <section class="ad ad--square">
    <div class="ad__sky" style="height:295px" role="img" aria-label="Sky above sunset clouds with a faint world map"></div>
    <div class="ad__subject" style="left:175px;top:42px;width:185px;height:318px" role="img" aria-label="Suitcase with an airplane window, plane, and a smiling traveller sitting with hat and float"></div>
    <div class="brand" style="left:45px;top:28px;font-size:24px">MILORA</div>
    <div class="headline" style="left:18px;top:86px;width:162px">
      <span class="headline__sell" style="font-size:32px">Sell us</span>
      <span class="headline__your" style="font-size:24px;margin-top:-6px">your</span>
      <span class="headline__airline" style="font-size:34px;margin-top:2px">AIRLINE</span>
      <span class="headline__miles" style="font-size:50px">MILES</span>
    </div>
    <div class="cta" style="left:45.6px;top:284px;width:98px;height:21.7px;font-size:13.5px">Get Quote</div>
  </section>
  <div class="size-label" style="left:225px;top:470px">1080 x 1080 pixels</div>

  <!-- 9:16 -->
  <section class="ad ad--story">
    <div class="ad__sky" style="height:530px" role="img" aria-label="Sky above sunset clouds with a faint world map"></div>
    <div class="ad__subject" style="left:80px;top:255px;width:210px;height:350px" role="img" aria-label="Suitcase with an airplane window, plane, and a smiling traveller sitting with hat and float"></div>
    <div class="brand" style="left:0;top:36px;width:360.6px;text-align:center;font-size:32px">MILORA</div>
    <div class="headline" style="left:0;top:86px;width:360.6px">
      <span class="headline__sell" style="font-size:35px">Sell us</span>
      <span class="headline__your" style="font-size:26px;margin-top:-8px">
        <svg width="54" height="2" style="vertical-align:middle;margin-right:4px"><line x1="0" y1="1" x2="54" y2="1" stroke="#ffffff" stroke-width="1"/></svg>your<svg width="46" height="2" style="vertical-align:middle;margin-left:4px"><line x1="0" y1="1" x2="46" y2="1" stroke="#ffffff" stroke-width="1"/></svg>
      </span>
      <span class="headline__airline" style="font-size:68px;margin-top:0">AIRLINE</span>
      <span class="headline__miles" style="font-size:70px;margin-top:-8px">MILES</span>
    </div>
    <div class="cta" style="left:125px;top:585px;width:123px;height:25px;font-size:16px">Get Quote</div>
  </section>
  <div class="size-label" style="left:669.5px;top:742px">1080 x 1920 pixels</div>

  <!-- 4:5 -->
  <section class="ad ad--portrait">
    <div class="ad__sky" style="height:355px" role="img" aria-label="Sky above sunset clouds with a faint world map"></div>
    <div class="ad__subject" style="left:182px;top:64px;width:178px;height:360px" role="img" aria-label="Suitcase with an airplane window, plane, and a smiling traveller sitting with hat and float"></div>
    <div class="brand" style="left:42px;top:54px;font-size:28px">MILORA</div>
    <div class="headline" style="left:18px;top:136px;width:162px">
      <span class="headline__sell" style="font-size:38px">Sell us</span>
      <span class="headline__your" style="font-size:26px;margin-top:-6px">your</span>
      <span class="headline__airline" style="font-size:34px;margin-top:4px">AIRLINE</span>
      <span class="headline__miles" style="font-size:50px">MILES</span>
    </div>
    <div class="cta" style="left:36px;top:372px;width:116px;height:25px;font-size:16px">Get Quote</div>
  </section>
  <div class="size-label" style="left:225px;top:1070px">1080 x 1350 pixels</div>

  <!-- 16:9 -->
  <section class="ad ad--landscape">
    <div class="ad__sky" style="height:189px" role="img" aria-label="Sky above sunset clouds with a faint world map"></div>
    <div class="ad__subject" style="left:270px;top:14px;width:142px;height:226px" role="img" aria-label="Suitcase with an airplane window, plane, and a smiling traveller sitting with hat and float"></div>
    <div class="brand" style="left:24px;top:32px;font-size:28px">MILORA</div>
    <div class="headline" style="left:20px;top:72px;text-align:left;white-space:nowrap">
      <span style="display:flex;align-items:baseline;gap:6px">
        <span class="headline__sell" style="display:inline;font-size:37px;color:var(--ink)">Sell us</span>
        <span class="headline__your" style="display:inline;font-size:30px">your</span>
      </span>
      <span style="display:flex;gap:8px;margin-top:2px">
        <span class="headline__airline" style="display:inline;font-size:36px">AIRLINE</span>
        <span class="headline__miles" style="display:inline;font-size:36px">MILES</span>
      </span>
    </div>
    <div class="cta" style="left:20px;top:179px;width:98px;height:21px;font-size:13.5px">Get Quote</div>
  </section>
  <div class="size-label" style="left:703px;top:1070px">1280 x 720 pixels</div>

</body>
</html>
```